Business Card Design

Non-profit organization creating opportunities for:
Personal empowerment
Community Outreach
Healthier Life Choices
Body/Mind/Spirit Nourishment
Emotional Transformation
Charity & Network Opportunities
Everyday people making An extrodinary sufferance
All achieved from the Source within YOU.
Organization logo is the ying yang symbol with a small circle above it as if it were the head and the ying yang symbol was the body.  Also in side upper ying needs to be a heart and in the lower yang needs to be the letter C. This is very important as it came to me in a dream n the forming of this organization.  Color choice is open although a thought I hade was that the heart is red metallic foil (sine a red heart is the symbol of love)and the c is gold foil( the gifts of the 3 wise men and gold being one of them).a verticle card is preferred and logo as large as possible on it even if ying yang is made oval Ilook forward to the layouts and designs you can come up with.

Industry/Entity Type
Business
Contact Information for Business Card
Lumina Harbor. Org
Peter Galvany
Executive Director
Lumina harbor.peter@mailbrook.net
315-482-9063

```html
<!DOCTYPE html>
<html lang="en">
<head>
<meta charset="utf-8">
<title>Lumina Harbor. Org — Business Card</title>
<link href="https://fonts.googleapis.com/css2?family=Mulish:ital,wght@0,400;0,700;0,800;1,400&display=swap" rel="stylesheet">
<style>
  :root {
    --backdrop: #6d6e71;
    --card: #ffffff;
    --ink: #111111;
    --heart-red: #e8323c;
    --gold: #8a7256;
  }
  * { margin: 0; padding: 0; box-sizing: border-box; }
  html, body {
    width: 1200px; height: 678px; overflow: hidden;
    background: var(--backdrop);
  }
  .canvas {
    position: relative; width: 1200px; height: 678px;
    font-family: "Mulish", "Century Gothic", sans-serif;
    color: var(--ink);
  }
  .card {
    position: absolute; top: 92px;
    width: 302px; height: 514px;
    background: var(--card);
  }
  .card--front { left: 278px; }
  .card--back { left: 624px; }

  /* front */
  .brand-mark {
    position: absolute; left: 0; right: 0; top: 140px;
    display: flex; flex-direction: column; align-items: center; gap: 18px;
  }
  .brand-mark__name {
    font-weight: 800; font-size: 28px; letter-spacing: 0.5px;
    text-align: center; line-height: 1.15;
  }
  .identity {
    position: absolute; left: 0; right: 0; top: 346px;
    text-align: center;
  }
  .identity__org { font-weight: 700; font-size: 17px; }
  .identity__person { margin-top: 20px; font-size: 17px; line-height: 21px; }
  .identity__title { display: block; font-style: italic; }
  .identity__contact { margin-top: 22px; font-weight: 700; font-size: 15px; line-height: 21px; }

  /* back */
  .mission {
    position: absolute; left: 28px; right: 20px; top: 30px;
    font-size: 16px; line-height: 19px;
  }
  .mission__intro { text-align: center; margin-left: -8px; }
  .mission__list { list-style: none; margin-top: 29px; }
  .mission__list li { padding-left: 0; }
  .mission__list li::before { content: "• "; }
  .mission__closing {
    margin-top: 20px; text-align: center; font-weight: 700;
    font-size: 16px; line-height: 21px; margin-left: -8px;
  }
  .mini-mark {
    position: absolute; left: 0; right: 0; top: 386px;
    display: flex; flex-direction: column; align-items: center; gap: 8px;
  }
  .mini-mark__name { font-weight: 800; font-size: 13px; }
</style>
</head>
<body>
<main class="canvas">
  <section class="card card--front">
    <div class="brand-mark">
      <svg width="150" height="150" viewBox="0 0 150 150" aria-hidden="true">
        <circle cx="75" cy="75" r="72" fill="none" stroke="var(--ink)" stroke-width="4"/>
      </svg>
      <span class="brand-mark__name">Lumina Harbor</span>
    </div>
    <div class="identity">
      <p class="identity__org">Lumina Harbor. Org</p>
      <p class="identity__person">Peter Galvany,<span class="identity__title">Executive Director</span></p>
      <p class="identity__contact">luminaharbor.peter@mailbrook.net<br>p. 315-482-9063</p>
    </div>
  </section>

  <section class="card card--back">
    <div class="mission">
      <p class="mission__intro">Non-profit organization<br>creating opportunities for:</p>
      <ul class="mission__list">
        <li>Personal empowerment</li>
        <li>Community Outreach</li>
        <li>Healthier Life Choices</li>
        <li>Body/Mind/Spirit Nourish-<br>ment</li>
        <li>Emotional Transformation</li>
        <li>Charity &amp; Network<br>Opportunities</li>
        <li>Everyday people making<br>An extrodinary sufferance</li>
      </ul>
      <p class="mission__closing">All achieved from<br>the Source within YOU.</p>
    </div>
    <div class="mini-mark">
      <svg width="66" height="66" viewBox="0 0 66 66" aria-hidden="true">
        <circle cx="33" cy="33" r="31" fill="none" stroke="var(--ink)" stroke-width="2.5"/>
      </svg>
      <span class="mini-mark__name">Lumina Harbor</span>
    </div>
  </section>
</main>
</body>
</html>
```